Working Capital graphics

Our business advisory firm requires 9 images to be re-created and improved in the branding of our business.

The 9 images have been uploaded below and the colours and branding of the business can be found at the website www.dunmorrowadvisory.com.au

```html
<!DOCTYPE html>
<html lang="en">
<head>
<meta charset="utf-8">
<title>Working Capital Drivers</title>
<link href="https://fonts.googleapis.com/css2?family=Poppins:ital,wght@0,400;0,500;0,700;0,800;1,700;1,800&family=Libre+Baskerville&display=swap" rel="stylesheet">
<style>
:root{
  --bg:#e6e6e6;
  --paper:#ffffff;
  --ink:#141414;
  --orange:#f7941d;
  --orange-deep:#f47a20;
  --red-orange:#ff4e0a;
  --blue:#0ab1ec;
  --blue-mid:#1c4fcb;
  --blue-royal:#0e3c8e;
  --navy:#0b2454;
  --box:#d9d9d9;
  --line:#8a8a8a;
  --ring:#b9c7de;
}
*{margin:0;padding:0;box-sizing:border-box}
html,body{width:1200px;height:884px;overflow:hidden;background:var(--bg)}
.canvas{position:relative;width:1200px;height:884px;font-family:'Poppins',sans-serif;color:var(--ink)}
.slide{position:absolute;background:var(--paper);box-shadow:4px 6px 10px rgba(0,0,0,.22)}
.slide svg{display:block;width:100%;height:100%}
.cash-cycle{left:162px;top:74px;width:394px;height:339px}
.receivables{left:621px;top:79px;width:512px;height:327px}
.inventories{left:58px;top:467px;width:508px;height:325px}
.payables{left:621px;top:467px;width:512px;height:327px}
text{font-family:'Poppins',sans-serif;fill:var(--ink)}
.label{font-size:19px}
.seg{font-size:19px;fill:#fff;text-anchor:middle}
.centre{font-family:'Libre Baskerville',serif;font-variant:small-caps;font-size:36px;text-anchor:middle}
.title{font-size:29px;font-weight:700}
.head{font-size:15px;font-weight:500}
.hub{font-size:18px}
.num{font-weight:800;font-style:italic}
.bar-text{fill:#fff;font-weight:700;font-style:italic}
.box-text{font-size:15px;text-anchor:middle}
.stem{stroke:var(--line);stroke-width:1.4;fill:none}
</style>
</head>
<body>
<div class="canvas">

  <!-- Cash cycle wheel -->
  <section class="slide cash-cycle">
    <svg viewBox="0 0 736 634">
      <circle cx="370" cy="316" r="237" fill="none" stroke="var(--ring)" stroke-width="2"/>
      <g class="wheel">
        <path d="M229.8 149 A218 218 0 0 1 362.4 98.1 L366.5 216.1 A100 100 0 0 0 305.7 239.4Z" fill="var(--blue)"/>
        <path d="M362.4 98.1 A218 218 0 0 1 532 170.2 L444.3 249.1 A100 100 0 0 0 366.5 216.1Z" fill="var(--orange)"/>
        <path d="M532 170.2 A218 218 0 0 1 572.1 397.7 L462.7 353.5 A100 100 0 0 0 444.3 249.1Z" fill="var(--orange-deep)"/>
        <path d="M572.1 397.7 A218 218 0 0 1 377.6 533.9 L373.5 415.9 A100 100 0 0 0 462.7 353.5Z" fill="var(--red-orange)"/>
        <path d="M377.6 533.9 A218 218 0 0 1 172.5 408.2 L279.4 358.3 A100 100 0 0 0 373.5 415.9Z" fill="var(--navy)"/>
        <path d="M172.5 408.2 A218 218 0 0 1 161.6 252.3 L274.4 286.8 A100 100 0 0 0 279.4 358.3Z" fill="var(--blue-royal)"/>
        <path d="M161.6 252.3 A218 218 0 0 1 229.8 149 L305.7 239.4 A100 100 0 0 0 274.4 286.8Z" fill="var(--blue-mid)"/>
      </g>
      <circle cx="370" cy="316" r="104" fill="#fff" stroke="#d6d6d6" stroke-width="8"/>
      <g class="beads" fill="#fff" stroke-width="3">
        <circle cx="296" cy="174" r="12"/><path d="M290 170 L298 170 L300 178" stroke="var(--blue)" fill="none"/>
        <circle cx="396" cy="158" r="12"/><path d="M393 152 L399 158 L393 164" stroke="var(--orange)" fill="none"/>
        <circle cx="498" cy="221" r="12"/><path d="M500 215 L500 223 L493 226" stroke="var(--orange)" fill="none"/>
        <circle cx="508" cy="396" r="12"/><path d="M502 394 L508 400 L514 394" stroke="var(--red-orange)" fill="none"/>
        <circle cx="368" cy="478" r="12"/><path d="M371 472 L365 478 L371 484" stroke="var(--navy)" fill="none"/>
        <circle cx="225" cy="369" r="12"/><path d="M219 373 L225 367 L231 371" stroke="var(--navy)" fill="none"/>
        <circle cx="223" cy="251" r="12"/><path d="M217 255 L223 249 L229 255" stroke="var(--blue-royal)" fill="none"/>
      </g>
      <text class="centre" x="370" y="306">Next $100</text>
      <text class="centre" x="370" y="342">of Sales</text>
      <text class="centre" x="370" y="378">Volume</text>

      <text class="seg" x="344" y="172">$0</text>
      <text class="seg" x="457" y="176">Cost of</text><text class="seg" x="457" y="195">Sales</text>
      <text class="seg" x="529" y="280">Operating</text><text class="seg" x="529" y="298">Expenses</text>
      <text class="seg" x="523" y="344">Fixed</text><text class="seg" x="523" y="363">Costs</text>
      <text class="seg" x="494" y="442">Tax</text>
      <text class="seg" x="465" y="466">Interest</text>
      <text class="seg" x="433" y="493">Dividends</text>
      <text class="seg" x="258" y="427">AR Days</text>
      <text class="seg" x="275" y="456">AP Days</text>
      <text class="seg" x="296" y="486">INV Days</text>
      <text class="seg" x="209" y="318">Additional</text><text class="seg" x="209" y="336">Debt</text>
      <text class="seg" x="244" y="212">Cash</text><text class="seg" x="244" y="230">Shortfall</text>

      <g fill="var(--blue)">
        <circle cx="370" cy="79" r="7"/><circle cx="370" cy="553" r="7"/>
        <circle cx="571" cy="191" r="7"/><circle cx="571" cy="440" r="7"/>
        <circle cx="169" cy="191" r="7"/><circle cx="169" cy="440" r="7"/>
      </g>
      <text class="label" x="370" y="55" text-anchor="middle">revenue $0</text>
      <text class="label" x="370" y="590" text-anchor="middle">revenue $0</text>
      <text class="label" x="601" y="175">Gross</text><text class="label" x="601" y="193">margin $0</text>
      <text class="label" x="596" y="457">EBIT $0</text>
      <text class="label" x="140" y="168" text-anchor="end">After</text>
      <text class="label" x="140" y="186" text-anchor="end">additional</text>
      <text class="label" x="140" y="204" text-anchor="end">funding $0</text>
      <text class="label" x="140" y="453" text-anchor="end">After working</text>
      <text class="label" x="140" y="472" text-anchor="end">capital $0</text>
    </svg>
  </section>

  <!-- Receivables drivers -->
  <section class="slide receivables">
    <svg viewBox="0 0 957 611">
      <defs>
        <filter id="soft" x="-30%" y="-30%" width="160%" height="160%"><feDropShadow dx="0" dy="0" stdDeviation="5" flood-color="#000" flood-opacity=".18"/></filter>
        <clipPath id="clipR"><rect width="957" height="611"/></clipPath>
      </defs>
      <text class="title" x="37" y="48">Receivables</text>
      <text class="head" x="259" y="47">Sub-Process</text>
      <text class="head" x="533" y="47" text-anchor="middle">Drivers</text>
      <text class="head" x="807" y="47" text-anchor="middle">Sub-Drivers</text>

      <g clip-path="url(#clipR)"><circle cx="30" cy="328" r="132" fill="#fff" filter="url(#soft)"/></g>
      <text class="hub" x="37" y="325">Receivables</text>
      <text class="hub" x="37" y="347">Drivers</text>

      <g fill="none" stroke-width="6">
        <path d="M75 177 Q140 205 172 238" stroke="var(--orange)"/>
        <path d="M165 252 Q205 330 165 410" stroke="var(--blue)"/>
        <path d="M75 478 Q140 455 172 425" stroke="var(--orange)"/>
      </g>
      <path d="M164 232 L182 228 L176 246Z" fill="var(--orange)"/>
      <path d="M192 321 L206 330 L192 339Z" fill="var(--blue)"/>
      <path d="M164 431 L182 436 L176 418Z" fill="var(--orange)"/>

      <circle cx="218" cy="193" r="40" fill="var(--orange)"/>
      <g stroke="#fff" stroke-width="2.5" fill="none">
        <rect x="203" y="175" width="24" height="32" rx="2"/>
        <path d="M208 188h14M208 195h14M208 201h9"/><circle cx="222" cy="178" r="5"/>
      </g>
      <circle cx="255" cy="328" r="40" fill="var(--blue)"/>
      <g stroke="#fff" stroke-width="2.5" fill="none">
        <circle cx="255" cy="328" r="15"/><path d="M255 317v22M260 321h-7a3.5 3.5 0 0 0 0 7h4a3.5 3.5 0 0 1 0 7h-7"/>
      </g>
      <circle cx="211" cy="467" r="40" fill="var(--orange)"/>
      <g stroke="#fff" stroke-width="2.5" fill="none">
        <circle cx="219" cy="457" r="9"/><path d="M193 477h8l10 5h14l8-7M201 483v-9"/>
      </g>
      <text x="268" y="201" font-size="22" fill="var(--orange)" style="fill:var(--orange)">Approval</text>
      <text x="302" y="336" font-size="22" style="fill:var(--blue)">Sales</text>
      <text x="256" y="484" font-size="22" style="fill:var(--orange)">Collections</text>

      <path d="M383 70V585" stroke="#bbb" stroke-width="1.5"/>

      <g class="bars">
        <path d="M436 73H650a17 17 0 0 1 0 34H430Z" fill="var(--orange)"/>
        <path d="M436 124H650a17 17 0 0 1 0 34H430Z" fill="var(--orange)"/>
        <path d="M436 175H650a17 17 0 0 1 0 34H430Z" fill="var(--orange)"/>
        <path d="M436 254H650a17 17 0 0 1 0 34H430Z" fill="var(--blue)"/>
        <path d="M436 308H650a17 17 0 0 1 0 34H430Z" fill="var(--blue)"/>
        <path d="M436 360H650a17 17 0 0 1 0 34H430Z" fill="var(--blue)"/>
        <path d="M436 442H650a17 17 0 0 1 0 34H430Z" fill="var(--orange)"/>
        <path d="M436 490H650a17 17 0 0 1 0 34H430Z" fill="var(--orange)"/>
        <path d="M436 544H650a17 17 0 0 1 0 34H430Z" fill="var(--orange)"/>
      </g>
      <g class="num" font-size="42">
        <text x="402" y="105" style="fill:var(--orange)">1</text>
        <text x="400" y="156" style="fill:var(--orange)">2</text>
        <text x="400" y="207" style="fill:var(--orange)">3</text>
        <text x="400" y="286" style="fill:var(--blue)">4</text>
        <text x="400" y="340" style="fill:var(--blue)">5</text>
        <text x="400" y="392" style="fill:var(--blue)">6</text>
        <text x="400" y="474" style="fill:var(--orange)">7</text>
        <text x="400" y="522" style="fill:var(--orange)">8</text>
        <text x="400" y="576" style="fill:var(--orange)">9</text>
      </g>
      <g class="bar-text" font-size="14">
        <text x="448" y="95">Differentiated terms</text>
        <text x="448" y="146">Customer agreements</text>
        <text x="448" y="197">Account set-up</text>
        <text x="445" y="276">Receipt process</text>
        <text x="445" y="330">Time to invoice</text>
        <text x="445" y="382">Customer payment behaviour</text>
        <text x="445" y="464">Payment cycle</text>
        <text x="445" y="512">Collections</text>
        <text x="445" y="566">Penalties</text>
      </g>

      <g class="stem">
        <path d="M667 325H682V121H712M682 149H712M682 196H712M682 227H712"/>
        <path d="M667 377H695V276H712M695 305H712M695 335H712"/>
        <path d="M667 459H682V391H712M682 421H712M682 450H712"/>
        <path d="M667 507H695V565H712M695 537H712M695 506H712"/>
      </g>
      <g fill="var(--box)">
        <rect x="712" y="111" width="187" height="20"/><rect x="712" y="139" width="187" height="20"/>
        <rect x="712" y="186" width="187" height="20"/><rect x="712" y="217" width="187" height="20"/>
        <rect x="712" y="266" width="187" height="20"/><rect x="712" y="295" width="187" height="20"/>
        <rect x="712" y="325" width="187" height="20"/><rect x="712" y="381" width="187" height="20"/>
        <rect x="712" y="411" width="187" height="20"/><rect x="712" y="440" width="187" height="20"/>
        <rect x="712" y="496" width="187" height="20"/><rect x="712" y="527" width="187" height="20"/>
        <rect x="712" y="555" width="187" height="20"/>
      </g>
      <g class="box-text">
        <text x="805" y="127">Cash</text><text x="805" y="155">Banking process</text>
        <text x="805" y="202">Sales delivery</text><text x="805" y="233">Invoicing</text>
        <text x="805" y="282">KPI</text><text x="805" y="311">Relationship</text>
        <text x="805" y="341">Pricing</text><text x="805" y="397">Closing date</text>
        <text x="805" y="427">Time to process</text><text x="805" y="456">Invoicing cycle</text>
        <text x="805" y="512">Tracking</text><text x="805" y="543">Methods</text>
        <text x="805" y="571">Agencies</text>
      </g>
    </svg>
  </section>

  <!-- Inventory drivers -->
  <section class="slide inventories">
    <svg viewBox="0 0 950 607">
      <defs>
        <filter id="softI" x="-30%" y="-30%" width="160%" height="160%"><feDropShadow dx="0" dy="0" stdDeviation="5" flood-color="#000" flood-opacity=".18"/></filter>
        <clipPath id="clipI"><rect width="950" height="607"/></clipPath>
      </defs>
      <text class="title" x="46" y="65" font-size="26" style="font-size:26px">Inventories</text>
      <text class="head" x="387" y="57" text-anchor="middle">Driver group</text>
      <text class="head" x="727" y="57" text-anchor="middle">Sub-Group</text>

      <g clip-path="url(#clipI)"><circle cx="56" cy="328" r="130" fill="#fff" filter="url(#softI)"/></g>
      <text x="46" y="318" font-size="23">Inventory</text>
      <text x="46" y="346" font-size="23">Drivers</text>

      <g stroke="var(--blue-royal)" stroke-width="1.3">
        <path d="M132 215L255 160M178 275L253 263M183 355L253 368M147 422L253 472"/>
      </g>
      <path d="M320 137H516a17 17 0 0 1 0 34H314Z" fill="var(--orange)"/>
      <path d="M320 243H516a17 17 0 0 1 0 34H314Z" fill="var(--blue)"/>
      <path d="M320 351H516a17 17 0 0 1 0 34H314Z" fill="var(--orange)"/>
      <path d="M320 456H516a17 17 0 0 1 0 34H314Z" fill="var(--blue)"/>
      <g class="num" font-size="46">
        <text x="260" y="171" style="fill:var(--orange)">10</text>
        <text x="262" y="277" style="fill:var(--blue)">11</text>
        <text x="260" y="385" style="fill:var(--orange)">12</text>
        <text x="260" y="491" style="fill:var(--blue)">13</text>
      </g>
      <g class="bar-text" font-size="17">
        <text x="328" y="160">Planning</text>
        <text x="328" y="266">Procurement</text>
        <text x="328" y="374">Fulfillment</text>
        <text x="328" y="479">Product range</text>
      </g>
      <g class="stem">
        <path d="M533 154H558M558 99V199M558 99H588M558 132H588M558 166H588M558 199H588"/>
        <path d="M533 260H558M558 243V309M558 243H588M558 277H588M558 309H588"/>
        <path d="M533 368H558M558 352V418M558 352H588M558 386H588M558 418H588"/>
        <path d="M533 473H558M558 464V531M558 464H588M558 499H588M558 531H588"/>
      </g>
      <g fill="var(--box)">
        <rect x="588" y="88" width="278" height="22"/><rect x="588" y="121" width="278" height="22"/>
        <rect x="588" y="155" width="278" height="22"/><rect x="588" y="188" width="278" height="22"/>
        <rect x="588" y="232" width="278" height="22"/><rect x="588" y="266" width="278" height="22"/>
        <rect x="588" y="298" width="278" height="22"/><rect x="588" y="341" width="278" height="22"/>
        <rect x="588" y="375" width="278" height="22"/><rect x="588" y="407" width="278" height="22"/>
        <rect x="588" y="453" width="278" height="22"/><rect x="588" y="488" width="278" height="22"/>
        <rect x="588" y="520" width="278" height="22"/>
      </g>
      <g class="box-text">
        <text x="727" y="105">Demand variability</text>
        <text x="727" y="138">Planning collaboration</text>
        <text x="727" y="172">Information availability</text>
        <text x="727" y="205">Inventory target setting</text>
        <text x="727" y="249">Order quantities</text>
        <text x="727" y="283">Supplier lead time variability</text>
        <text x="727" y="315">Supplier quality variability</text>
        <text x="727" y="358">Customer service levels</text>
        <text x="727" y="392">Network structure</text>
        <text x="727" y="424">Inventory postponement</text>
        <text x="727" y="470">Customer inventory needs</text>
        <text x="720" y="505">Part standardisation</text>
        <text x="722" y="537">SKU proliferation</text>
      </g>
    </svg>
  </section>

  <!-- Payables drivers -->
  <section class="slide payables">
    <svg viewBox="0 0 957 610">
      <defs>
        <filter id="softP" x="-30%" y="-30%" width="160%" height="160%"><feDropShadow dx="0" dy="0" stdDeviation="5" flood-color="#000" flood-opacity=".18"/></filter>
        <clipPath id="clipP"><rect width="957" height="610"/></clipPath>
      </defs>
      <text class="title" x="47" y="67" style="font-size:26px">Payables</text>
      <text x="577" y="60" font-size="24" font-weight="500" text-anchor="middle">Drivers</text>

      <g clip-path="url(#clipP)"><circle cx="57" cy="328" r="132" fill="#fff" filter="url(#softP)"/></g>
      <text x="47" y="318" font-size="24">Payables</text>
      <text x="47" y="348" font-size="24">Drivers</text>

      <g stroke="var(--blue-royal)" stroke-width="1.3" fill="none">
        <path d="M189 328H289M289 135V502M289 135H342M289 224H342M289 312H342M289 412H342M289 502H342"/>
      </g>
      <path d="M424 112H780a23 23 0 0 1 0 46H416Z" fill="var(--orange)"/>
      <path d="M424 200H780a23 23 0 0 1 0 46H416Z" fill="var(--blue)"/>
      <path d="M424 288H780a23 23 0 0 1 0 46H416Z" fill="var(--orange)"/>
      <path d="M416 378H780a23 23 0 0 1 0 46H406Z" fill="var(--blue)"/>
      <path d="M424 474H780a23 23 0 0 1 0 46H416Z" fill="var(--blue)"/>
      <g class="num" font-size="62">
        <text x="350" y="158" style="fill:var(--orange)">14</text>
        <text x="350" y="246" style="fill:var(--blue)">15</text>
        <text x="350" y="334" style="fill:var(--orange)">16</text>
        <text x="350" y="430" style="fill:var(--blue)">17</text>
        <text x="350" y="524" style="fill:var(--blue)">18</text>
      </g>
      <g class="bar-text" font-size="25">
        <text x="444" y="144">Reduce early payments</text>
        <text x="444" y="232">Reduce over-rides</text>
        <text x="444" y="320">Reduce vendor credits</text>
        <text x="444" y="410">Increase PO vendor terms</text>
        <text x="444" y="506">Increase invoice only terms</text>
      </g>
    </svg>
  </section>

</div>
</body>
</html>
```